Business Card Design Project

We need a business card for our business called Our Harbour Lender. (www.ourharbourlender.com.au)

There are 3 of us in the business, the design we choose will stay the same for all 3 of us, but will need names changed and mobile numbers added. I will provide details in an attachment.

We are a professional services directory for mortgage brokers. I will attach an idea that I had, but happy for you to be free in your designs. We would like the colour scheme to remain within our company colours - blue, white, grey and orange.

Thanks so much for helping us with this project. If you need anymore information, please don't hesitate to ask.

Industry/Entity Type

Business

Requirements
Must have
• Our Harbour Lender Logo
Colour blue and orange to match closely with our logo samples if possible.
The most important card is the card for Tilda Brennan

```html
<!DOCTYPE html>
<html lang="en">
<head>
<meta charset="utf-8">
<title>Our Harbour Lender – Business Card</title>
<link rel="stylesheet" href="https://fonts.googleapis.com/css2?family=Arimo:wght@400;700&display=swap">
<style>
  :root {
    --brand-blue: #2f8bc9;
    --brand-blue-deep: #2a7fb9;
    --ink-blue: #2d86c4;
    --card-white: #f7f7f7;
    --card-grey: #e4e4e4;
    --icon-grey: #3a3a3a;
    --stage: #e9eaec;
  }
  * { box-sizing: border-box; margin: 0; padding: 0; }
  html, body { width: 1200px; height: 900px; overflow: hidden; }
  body {
    background: var(--stage);
    font-family: "Arimo", Arial, sans-serif;
    display: flex;
    flex-direction: column;
    align-items: center;
    justify-content: center;
    gap: 48px;
  }
  .card {
    width: 580px;
    height: 354px;
    position: relative;
    box-shadow: 0 6px 18px rgba(0,0,0,0.12);
    overflow: hidden;
  }

  /* Back side */
  .card-back {
    background: var(--brand-blue);
    display: flex;
    align-items: center;
    justify-content: center;
    gap: 18px;
  }
  .brand-dot {
    width: 54px; height: 54px;
    border-radius: 50%;
    background: #ffffff;
  }
  .brand-name {
    color: #ffffff;
    font-size: 44px;
    font-weight: 400;
    letter-spacing: -0.5px;
  }

  /* Front side */
  .card-front {
    background: radial-gradient(circle at 30% 20%, var(--card-white) 0%, #efefef 55%, var(--card-grey) 100%);
    padding: 38px 40px 0 44px;
  }
  .holder-name {
    color: var(--ink-blue);
    font-size: 34px;
    font-weight: 700;
    letter-spacing: 0.5px;
    line-height: 1;
  }
  .holder-role {
    color: var(--ink-blue);
    font-size: 25px;
    font-weight: 400;
    letter-spacing: 0.5px;
    margin-top: 4px;
  }
  .contact-list {
    list-style: none;
    margin-top: 34px;
    margin-left: 22px;
  }
  .contact-list li {
    display: flex;
    align-items: center;
    gap: 14px;
    color: var(--ink-blue);
    font-size: 16px;
    line-height: 22px;
  }
  .contact-list svg { width: 16px; height: 16px; fill: var(--icon-grey); flex: none; }
  .legal-note {
    position: absolute;
    left: 40px;
    bottom: 34px;
    color: var(--ink-blue);
    font-size: 11px;
    line-height: 14px;
  }
  .brand-mark {
    position: absolute;
    right: 70px;
    top: 162px;
    width: 110px; height: 110px;
    border-radius: 50%;
    border: 12px solid var(--brand-blue);
  }
</style>
</head>
<body>

  <section class="card card-back" aria-label="Card back">
    <span class="brand-dot" aria-hidden="true"></span>
    <span class="brand-name">Our Harbour Lender</span>
  </section>

  <section class="card card-front" aria-label="Card front">
    <h1 class="holder-name">TILDA BRENNAN</h1>
    <p class="holder-role">CEO / FOUNDER</p>

    <ul class="contact-list">
      <li>
        <svg viewBox="0 0 16 16" aria-hidden="true"><path d="M1 5c0-2 3-3 7-3s7 1 7 3v1.5h-3.5V5h-7v1.5H1z M3 8h10l1 6H2z"/></svg>
        1300 HARBOUR
      </li>
      <li>
        <svg viewBox="0 0 16 16" aria-hidden="true"><rect x="4.5" y="1" width="7" height="14" rx="1.5"/><rect x="6" y="3" width="4" height="7" fill="#f2f2f2"/></svg>
        0400 318 275
      </li>
      <li>
        <svg viewBox="0 0 16 16" aria-hidden="true"><path d="M4 1.5l3 3-1.6 1.6a9 9 0 0 0 4.5 4.5L11.5 9l3 3-2 2.5C6.5 14 2 9.5 1.5 3.5z"/></svg>
        02 9164 2058
      </li>
      <li>
        <svg viewBox="0 0 16 16" aria-hidden="true"><path d="M1 3h14v10H1z"/><path d="M1.5 3.5L8 9l6.5-5.5" stroke="#f2f2f2" stroke-width="1.4" fill="none"/></svg>
        tilda@harbourlender.com
      </li>
      <li>
        <svg viewBox="0 0 16 16" aria-hidden="true"><circle cx="8" cy="8" r="7"/><path d="M1 8h14M8 1c-3 3.5-3 10.5 0 14M8 1c3 3.5 3 10.5 0 14" stroke="#f2f2f2" stroke-width="1.1" fill="none"/></svg>
        www.ourharbourlender.com.au
      </li>
    </ul>

    <p class="legal-note">Our Harbour Lender is a Bayline Finance Group Pty Ltd project<br>ABN 41 207 553 918</p>

    <span class="brand-mark" aria-hidden="true"></span>
  </section>

</body>
</html>
```